Business Card Design Project

I need a new business card design for my Remodel/Design/Build company, Northgate Home Improvement, Inc. See our website: www.northgatehomeimprovement-example.com
We are an established company with a growing reputation and growing quickly. We are know for being on the forward edge of the industry, producing a great product and our "people friendly" approach.
I am looking for something cool, transitional, maybe even retro that captures the imagination, shows our sleek creativity and streamlined approach as well as communicates stability and trustworthiness.
Updates

Stainless steel business card design would be cool.

Please have all future designs with full logo colors and shown on a stainless steel business card.  Also, logo and tag line will most likely be printed with spot uv, so layers will be necessary.  Thank you.

Target Market(s)

30-65 yrs old, homeowners, appreciate fine things, median income $150+k, net worth $1+m

Industry/Entity Type

Business

Requirements
Must have
• Company Logo
Contact information
Website URL
Nice to have
• Tagline: Building Relationships and Remodeling Homes...One Client at a Time.
Double-sided okay.
Stainless steel business card.

```html
<!DOCTYPE html>
<html lang="en">
<head>
<meta charset="utf-8">
<title>Northgate Home Improvement – Business Card</title>
<link rel="stylesheet" href="https://fonts.googleapis.com/css2?family=Jost:wght@400;500&display=swap">
<style>
  :root {
    --page: #e4e4e4;
    --cream: #f3efbd;
    --wine: #8e1116;
    --wine-deep: #6f0b10;
    --gold: #e2b83a;
    --gold-deep: #c9962a;
  }
  * { box-sizing: border-box; margin: 0; padding: 0; }
  html, body { width: 1200px; height: 900px; overflow: hidden; }
  body {
    background: var(--page);
    font-family: "Jost", "Helvetica Neue", Arial, sans-serif;
    display: flex; align-items: center; justify-content: center; gap: 40px;
  }
  .card {
    position: relative; width: 540px; height: 309px; overflow: hidden;
    box-shadow: 0 8px 24px rgba(0,0,0,.22);
  }

  /* ---------- back side ---------- */
  .card--back { background: var(--wine); }
  .gallery {
    position: absolute; left: 14px; top: 14px; width: 296px; height: 281px;
    display: grid; grid-template-columns: 1fr 1fr; grid-template-rows: 1fr 1fr; gap: 10px;
  }
  .gallery__photo--kitchen { background: linear-gradient(135deg, #6b3a1c, #b06a35 55%, #4a2412); }
  .gallery__photo--dining { background: linear-gradient(135deg, #3a2a22, #a0693d 60%, #5b3d2a); }
  .gallery__photo--bath { background: linear-gradient(135deg, #8c7a3a, #d8c77a 50%, #6d5f2c); }
  .gallery__photo--archway { background: linear-gradient(135deg, #5a4434, #a68266 55%, #3b2a1f); }
  .back__brand {
    position: absolute; left: 320px; top: 14px; right: 14px; height: 136px;
    background: var(--cream); display: flex; align-items: center; gap: 10px; padding: 0 12px;
  }
  .back__info {
    position: absolute; left: 320px; right: 14px; top: 172px;
    color: var(--gold); text-align: center;
  }
  .back__tagline { font-size: 10px; line-height: 1.6; white-space: nowrap; }
  .back__web { font-size: 9px; margin-top: 22px; font-weight: 500; white-space: nowrap; }

  /* ---------- company name stand-in ---------- */
  .brand__dot { flex: none; width: 26px; height: 26px; border-radius: 50%; background: var(--wine); }
  .brand__name {
    color: var(--wine); font-weight: 500; text-transform: uppercase;
    letter-spacing: .02em; line-height: 1.15; white-space: nowrap;
  }
  .back__brand .brand__name { font-size: 12.5px; }

  /* ---------- front side ---------- */
  .card--front { background: var(--cream); }
  .front__brand {
    position: absolute; left: 22px; top: 34px; display: flex; align-items: center; gap: 14px;
  }
  .front__brand .brand__dot { width: 46px; height: 46px; }
  .front__brand .brand__name { font-size: 22px; letter-spacing: .04em; }
  .front__accent {
    position: absolute; left: 22px; top: 222px; width: 136px; height: 72px;
    background: linear-gradient(135deg, var(--gold), var(--gold-deep));
  }
  .front__band {
    position: absolute; left: 168px; right: 12px; top: 152px; bottom: 14px;
    background: linear-gradient(90deg, var(--wine-deep), var(--wine));
  }
  .person { position: absolute; right: 24px; top: 118px; text-align: right; }
  .person__name { color: var(--wine); font-size: 25px; font-weight: 500; line-height: 1.1; }
  .person__title { color: var(--gold); font-size: 18px; margin-top: 8px; }
  .contact {
    position: absolute; right: 24px; top: 198px; text-align: right;
    color: var(--gold); font-size: 12.5px; line-height: 1.45; white-space: nowrap;
  }
  .contact b { font-weight: 500; }
  .front__tagline {
    position: absolute; right: 24px; bottom: 26px; color: var(--gold); font-size: 8.5px; white-space: nowrap;
  }
</style>
</head>
<body>

  <section class="card card--back" aria-label="Business card, back">
    <div class="gallery">
      <div class="gallery__photo gallery__photo--kitchen" role="img" aria-label="Photo of a remodeled wood kitchen"></div>
      <div class="gallery__photo gallery__photo--dining" role="img" aria-label="Photo of a kitchen with dining table"></div>
      <div class="gallery__photo gallery__photo--bath" role="img" aria-label="Photo of a remodeled bathroom vanity"></div>
      <div class="gallery__photo gallery__photo--archway" role="img" aria-label="Photo of a stone archway interior"></div>
    </div>
    <div class="back__brand">
      <span class="brand__dot"></span>
      <span class="brand__name">Northgate<br>Home Improvement</span>
    </div>
    <div class="back__info">
      <p class="back__tagline">Crafting Trust and Renewing Spaces…<br>One Household at a Time</p>
      <p class="back__web">www.northgatehomeimprovement-example.com</p>
    </div>
  </section>

  <section class="card card--front" aria-label="Business card, front">
    <div class="front__brand">
      <span class="brand__dot"></span>
      <span class="brand__name">Northgate<br>Home Improvement</span>
    </div>
    <div class="front__accent"></div>
    <div class="front__band"></div>
    <div class="person">
      <p class="person__name">Dana Whitfield</p>
      <p class="person__title">President</p>
    </div>
    <div class="contact">
      <p><b>ph</b> 555-013-8815 <b>fax</b> 555-013-8816 <b>mobile</b> 555-019-2240</p>
      <p><b>email</b> dwhitfield@northgatehomeimprovement-example.com</p>
    </div>
    <p class="front__tagline">Crafting Trust and Renewing Spaces…One Household at a Time</p>
  </section>

</body>
</html>
```